Website for IT consulting Company

I need a website upgrade, the existing site content is ok, I would also like to add a testimonial page, the site should be something that is easy for us to update content. You use the content from www.velmarketa.com as an example. I will also post update logo and artwork. I also need a contact form with some type of validation or captcha.

Please omit Address maps

Target Market(s)

small business, service oriented companies. We provide IT Consulting, support and mangement

Industry/Entity Type

Information Technology

Coding

Coded - Design and coding required

Number of Pages Required

1 page

Font styles to use
Serif
Sans Serif

Requirements
Must have
• Contain logo attached, and content from existing web site www.velmarketa.com.
• Also need to update content easily, and be movable to different platforms.
• There is a catch phrase
• "Let us worry about your technology…” “ so you don’t have to!”
• Should be included.
Nice to have
• Testimonial page, Project page where we can post new and past projects and pictures
Should not have
• none

```html
<!DOCTYPE html>
<html lang="en">
<head>
<meta charset="utf-8">
<title>Velmarketa – IT Solutions</title>
<link href="https://fonts.googleapis.com/css2?family=Lato:wght@400;700;900&family=Lora:ital@0;1&display=swap" rel="stylesheet">
<style>
:root{
  --orange:#f0862a;
  --ink:#222;
  --text:#444;
  --muted:#999;
  --dark:#3b3b3d;
  --header:#1e2126;
  --panel:#ededed;
  --light:#f4f4f4;
  --white:#fff;
}
*{box-sizing:border-box;margin:0;padding:0}
html,body{width:1200px;height:4196px;overflow:hidden}
body{position:relative;font-family:'Lato',sans-serif;color:var(--text);background:var(--white)}
.abs{position:absolute}
section,header,footer{position:absolute;left:0;width:1200px}

.topbar{top:0;height:28px;background:var(--orange);color:var(--white);font-size:13px}
.topbar .addr{left:98px;top:6px}
.topbar .addr svg{vertical-align:-2px;margin-right:8px}
.social-mini{right:25px;top:5px;display:flex;gap:6px}
.social-mini span{width:18px;height:18px;border-radius:50%;border:1.5px solid var(--white)}

.site-header{top:28px;height:117px;background:var(--header)}
.brand{left:98px;top:30px;display:flex;align-items:center;gap:12px}
.brand .mark{width:52px;height:52px;background:var(--orange)}
.brand .name{font-weight:900;font-size:40px;color:var(--white);letter-spacing:1px}
.phone{left:783px;top:44px;display:flex;align-items:center;gap:14px;color:var(--white);font-size:22px;font-weight:700}
.phone .ico{width:28px;height:28px;background:var(--orange);border-radius:4px;display:flex;align-items:center;justify-content:center}
.burger{left:1052px;top:44px;width:38px}
.burger span{display:block;height:5px;background:var(--orange);margin-bottom:7px;border-radius:2px}
.dropdown{left:943px;top:154px;width:162px;background:var(--orange);z-index:5;padding:6px 0 10px;box-shadow:0 4px 10px rgba(0,0,0,.3)}
.dropdown li{list-style:none;color:var(--white);font-size:14px;padding:7px 16px;text-transform:uppercase}
.dropdown li.active{background:var(--light);color:var(--ink)}
.dropdown li::before{content:"›";margin-right:8px}

.hero{top:145px;height:448px;background:linear-gradient(90deg,#152232 0%,#1f3650 45%,#34587a 75%,#2a4666 100%)}
.hero .visual{right:0;top:0;width:700px;height:448px;background:radial-gradient(ellipse at 60% 45%,#7ea4c6 0%,#3b6387 40%,rgba(31,54,80,0) 75%)}
.hero h1{left:98px;top:112px;color:var(--white);font-weight:900;line-height:1.15}
.hero h1 .l1{display:block;font-size:31px}
.hero h1 .l2{display:block;font-size:42px}
.hero .sub{left:98px;top:206px;color:var(--white);font-size:23px;letter-spacing:.5px}
.btn-outline{display:inline-block;border:2px solid var(--white);color:var(--white);font-size:15px;padding:12px 34px;border-radius:3px}
.hero .btn-outline{left:98px;top:258px}
.dots{left:560px;top:395px;display:flex;gap:10px}
.dots span{width:12px;height:12px;border-radius:50%;background:var(--white)}
.dots span:first-child{background:var(--orange)}

.services{top:593px;height:357px}
.service{top:80px;width:320px}
.service .head{display:flex;align-items:center;gap:14px;font-weight:900;font-size:14px;color:var(--ink);text-transform:uppercase;white-space:nowrap}
.service .head svg{flex:none}
.service p{margin-top:18px;font-size:15px;line-height:1.55;width:300px}
.readmore{margin-top:22px;font-size:14px;color:var(--ink);display:flex;align-items:center;gap:8px}
.readmore i{width:22px;height:22px;border-radius:50%;border:2px solid var(--orange);display:inline-flex;align-items:center;justify-content:center;color:var(--orange);font-style:normal;font-size:13px}

.welcome{top:950px;height:359px;background:var(--orange);color:var(--white);text-align:center}
.welcome h2{margin-top:58px;font-size:31px;font-weight:900;letter-spacing:1px}
.welcome p{width:1020px;margin:24px auto 0;font-size:16px;line-height:1.7}
.welcome .btn-outline{margin-top:28px}

.support{top:1309px;height:649px}
.topic{width:200px;font-size:13px;line-height:1.4;color:var(--muted)}
.topic b{display:block;font-weight:400;font-size:15px;color:var(--ink);text-transform:uppercase;white-space:nowrap}
.topic.hl b{color:var(--orange)}

.flex-sol{top:1958px;height:447px}
.flex-sol .panel{left:475px;top:0;width:672px;height:405px;background:var(--panel)}
.flex-sol .photo{left:98px;top:33px;width:503px;height:344px;background:linear-gradient(135deg,#2a3340,#7c8a99 55%,#cfd6de)}
.flex-sol h2{left:649px;top:30px;width:480px;font-size:30px;font-weight:900;color:var(--ink);line-height:1.15;text-transform:uppercase}
.flex-sol .body{left:649px;top:112px;width:470px;font-size:16px;line-height:1.6;color:var(--text)}
.flex-sol .list{left:649px;top:300px;font-size:14px;display:flex;gap:60px;text-transform:uppercase}
.btn-orange-outline{left:649px;top:336px;border:2px solid var(--orange);color:var(--ink);font-size:15px;padding:12px 32px;border-radius:3px}

.catch{top:2405px;height:358px}
.catch .photo{left:500px;top:0;width:700px;height:358px;background:linear-gradient(120deg,#c5ccd4,#7d8b9a 50%,#4a5564)}
.catch svg{left:0;top:0}
.catch blockquote{left:60px;top:110px;width:440px;color:var(--white);font-weight:900;font-size:31px;text-align:center;line-height:1.2;text-transform:uppercase}

.testimonials{top:2763px;height:537px}
.testimonials h2{position:absolute;width:100%;top:60px;text-align:center;font-size:29px;font-weight:900;color:var(--ink)}
.card{top:148px;width:300px;text-align:center}
.card .avatar{width:186px;height:186px;border-radius:50%;margin:0 auto;background:linear-gradient(160deg,#888,#2c2c2c)}
.card .name{margin-top:22px;font-size:22px;color:var(--ink)}
.card .name b{font-weight:900}
.card q{display:block;margin:6px auto 0;width:260px;font-family:'Lora',serif;font-size:15px;line-height:1.4;color:var(--text);quotes:"\201C" "\201D"}
.card .who{font-size:15px;color:#1b7bbf;margin-top:4px}
.card .readmore{justify-content:center;margin-top:10px}

.newsletter{top:3300px;height:182px;background:var(--light);text-align:center}
.newsletter h2{margin-top:40px;font-size:27px;font-weight:900;color:var(--ink)}
.newsletter .tag{font-size:14px;letter-spacing:1px;color:var(--ink)}
.newsletter form{position:absolute;left:336px;top:114px;display:flex}
.newsletter .field{width:425px;height:24px;border:1px solid #ccc;background:var(--white);font-size:11px;color:#666;text-align:left;padding:5px 8px}
.newsletter .go{width:95px;height:24px;background:var(--orange);color:var(--white);font-size:13px;font-weight:700;line-height:24px}

.contact{top:3482px;height:658px;background:var(--dark);color:var(--white)}
.contact h2{position:absolute;width:100%;top:62px;text-align:center;font-size:25px;font-weight:700}
.input{background:var(--white);color:#666;font-size:15px;padding:10px 12px;height:40px}
.submit{left:534px;top:350px;width:160px;height:46px;background:var(--orange);color:var(--white);font-weight:700;font-size:15px;text-align:center;line-height:46px}
.info{top:440px;width:300px;text-align:center;font-size:17px}
.info .ring{width:68px;height:68px;border:2px solid var(--white);border-radius:50%;margin:0 auto 24px;display:flex;align-items:center;justify-content:center}
.social{left:469px;top:592px;display:flex;gap:16px}
.social span{width:42px;height:42px;border:2px solid var(--white);border-radius:50%}

.site-footer{top:4140px;height:56px;background:var(--orange);color:var(--white);text-align:center;font-size:16px;line-height:56px}
</style>
</head>
<body>

<div class="topbar">
  <div class="abs addr"><svg width="10" height="14" viewBox="0 0 10 14"><path d="M5 0a5 5 0 0 1 5 5c0 4-5 9-5 9S0 9 0 5a5 5 0 0 1 5-5z" fill="#fff"/><circle cx="5" cy="5" r="2" fill="#f0862a"/></svg>123 Street, City Name, DC 12345</div>
  <div class="abs social-mini"><span></span><span></span><span></span><span></span><span></span></div>
</div>

<header class="site-header">
  <div class="abs brand"><div class="mark"></div><div class="name">VELMARKETA</div></div>
  <div class="abs phone"><span class="ico"><svg width="16" height="16" viewBox="0 0 24 24"><path d="M6.6 10.8a15 15 0 0 0 6.6 6.6l2.2-2.2c.3-.3.7-.4 1-.2 1.1.4 2.300.6 3.6.6.6 0 1 .4 1 1V20c0 .6-.4 1-1 1A17 17 0 0 1 3 4c0-.6.4-1 1-1h3.5c.6 0 1 .4 1 1 0 1.3.2 2.5.6 3.6.1.3 0 .7-.2 1z" fill="#fff"/></svg></span>123-4567-8910</div>
  <div class="abs burger"><span></span><span></span><span></span></div>
</header>

<ul class="abs dropdown">
  <li class="active">Home</li><li>About</li><li>Contact</li><li>Support</li><li>Clients</li><li>Careers</li>
</ul>

<section class="hero">
  <div class="abs visual" role="img" aria-label="Hand holding a tablet with glowing network connections"></div>
  <h1 class="abs"><span class="l1">IT SOLUTIONS THAT WORK FOR</span><span class="l2">YOUR BUSINESS..</span></h1>
  <div class="abs sub">A FULL SERVICE TECHNOLOGY COMPANY</div>
  <a class="abs btn-outline">Read More</a>
  <div class="abs dots"><span></span><span></span><span></span><span></span></div>
</section>

<section class="services">
  <div class="abs service" style="left:98px">
    <div class="head"><svg width="44" height="44" viewBox="0 0 44 44"><circle cx="22" cy="12" r="8" fill="#f0862a"/><path d="M8 40c0-10 6-16 14-16s14 6 14 16z" fill="#f0862a"/></svg>Managed IT Solutions</div>
    <p>Our staff will design, service, administer and maintain your IT needs. We are well versed on all major operating system, and network appliances...</p>
    <div class="readmore">Read More... <i>→</i></div>
  </div>
  <div class="abs service" style="left:462px">
    <div class="head"><svg width="44" height="44" viewBox="0 0 44 44"><path d="M8 36 30 14" stroke="#f0862a" stroke-width="6" stroke-linecap="round"/><circle cx="32" cy="12" r="7" fill="none" stroke="#f0862a" stroke-width="4"/></svg>Remote Diagnostic &amp;Support</div>
    <p>Do you need a quick solution to a technical problem? With our live remote-assistance tool, a member of our support team can view your desktop and share control ...</p>
    <div class="readmore">Read More... <i>→</i></div>
  </div>
  <div class="abs service" style="left:839px">
    <div class="head"><svg width="44" height="44" viewBox="0 0 44 44"><circle cx="22" cy="22" r="18" fill="#f0862a"/><circle cx="22" cy="22" r="7" fill="#fff"/></svg>IT Infrastructure Design</div>
    <p>Do you have more than one site? Do you need remote access? We can design and implement LANS/WANS and VPN's. Make your ...</p>
    <div class="readmore">Read More... <i>→</i></div>
  </div>
</section>

<section class="welcome">
  <h2>WELCOME TO VELMARKETA</h2>
  <p>Outsourcing is subcontracting a process, such as product design or manufacturing, to a third-party company.[1] The decision to outsource is often made in the interest of lowering firm costs, redirecting or conserving energy directed at the competencies of a particular business, or to make more efficient use of land, labor, capital, (information) technology and resources. Outsourcing became part of the business lexicon during the 1980s</p>
  <a class="btn-outline">Read More</a>
</section>

<section class="support">
  <svg class="abs" style="left:0;top:0" width="1200" height="649" viewBox="0 0 1200 649">
    <g stroke="#333" stroke-width="2" fill="none">
      <path d="M598 150 V138"/>
      <path d="M700 196 L760 152 H930"/>
      <path d="M762 313 H825"/>
      <path d="M700 430 L760 452 H930"/>
      <path d="M598 476 V552"/>
      <path d="M496 430 L440 466 H168"/>
      <path d="M434 313 H420"/>
      <path d="M496 196 L440 172 H137"/>
    </g>
    <circle cx="598" cy="313" r="150" fill="none" stroke="#3a3a3a" stroke-width="24" stroke-dasharray="100 135.6" stroke-dashoffset="-117.8" transform="rotate(-103 598 313)"/>
    <circle cx="598" cy="313" r="150" fill="none" stroke="#f0862a" stroke-width="24" stroke-dasharray="100 135.6" transform="rotate(-103 598 313)"/>
    <text x="598" y="312" text-anchor="middle" font-family="Lato,sans-serif" font-weight="900" font-size="32" fill="#222">IT SUPPORT</text>
    <text x="598" y="340" text-anchor="middle" font-family="Lato,sans-serif" font-size="17" letter-spacing="2" fill="#222">SOLUTIONS</text>
  </svg>
  <div class="abs topic hl" style="left:503px;top:84px"><b>Network Administration</b>LoLorem ipsum dolor sit amet, consectetur adipiscing elit, sed</div>
  <div class="abs topic" style="left:870px;top:160px"><b>Desktop Support</b>LoLorem ipsum dolor sit amet, consectetur adipiscing elit, sed</div>
  <div class="abs topic hl" style="left:831px;top:300px"><b>Network Cabling</b>LoLorem ipsum dolor sit amet, consectetur adipiscing elit, sed</div>
  <div class="abs topic" style="left:873px;top:460px"><b>Antivirus Solutions</b>LoLorem ipsum dolor sit amet, consectetur adipiscing elit, sed</div>
  <div class="abs topic hl" style="left:537px;top:562px"><b>Disaster Recovery</b>LoLorem ipsum dolor sit amet, consectetur adipiscing elit, sed</div>
  <div class="abs topic" style="left:168px;top:474px"><b>Telecommunications</b>LoLorem ipsum dolor sit amet, consectetur adipiscing elit, sed</div>
  <div class="abs topic hl" style="left:220px;top:300px;width:190px"><b>Web Design</b>LoLorem ipsum dolor sit amet, consectetur adipiscing elit, sed</div>
  <div class="abs topic" style="left:137px;top:180px"><b>Network Security</b>LoLorem ipsum dolor sit amet, consectetur adipiscing elit, sed</div>
</section>

<section class="flex-sol">
  <div class="abs panel"></div>
  <div class="abs photo" role="img" aria-label="Technician with a laptop in a server room"></div>
  <h2 class="abs">Flexible Solutions for your Business Needs</h2>
  <p class="abs body">Velmarketa is a technology solution provider based in Brenford, Calvera. Our goal is to make technology a non-issue for individuals and small to medium size businesses ranging from 5 to 150 Users. Velmarketa has the experience, the tools, high-level technology solutions and training to power your business and your work force. We understand that all business's have one goal in common!</p>
  <div class="abs list"><span>&gt; Disaster Recovery</span><span>&gt; Audio/Video Multimedia.</span></div>
  <a class="abs btn-orange-outline">Read More</a>
</section>

<section class="catch">
  <div class="abs photo" role="img" aria-label="Business team discussing around a laptop"></div>
  <svg class="abs" width="780" height="358" viewBox="0 0 780 358"><polygon points="0,0 545,0 760,358 0,358" fill="#f0862a"/></svg>
  <blockquote class="abs">“Let us worry about your technology...”<br>“ So you don’t have to!”</blockquote>
</section>

<section class="testimonials">
  <h2>TESTIMONIAL</h2>
  <div class="abs card" style="left:102px"><div class="avatar" role="img" aria-label="Client portrait"></div><div class="name"><b>NAME,</b> DIRECTOR</div><q>Lorem ipsum dolor amet conse ctetur dolore elit,sed do eiusmod tempor et dolore magna.</q><div class="who">Lorem ipsum dolor</div><div class="readmore">read more... <i>→</i></div></div>
  <div class="abs card" style="left:460px"><div class="avatar" role="img" aria-label="Client portrait"></div><div class="name"><b>NAME,</b> DIRECTOR</div><q>Lorem ipsum dolor amet conse ctetur dolore elit,sed do eiusmod tempor et dolore magna.</q><div class="who">Lorem ipsum dolor</div><div class="readmore">read more... <i>→</i></div></div>
  <div class="abs card" style="left:829px"><div class="avatar" role="img" aria-label="Client portrait"></div><div class="name"><b>NAME,</b> DIRECTOR</div><q>Lorem ipsum dolor amet conse ctetur dolore elit,sed do eiusmod tempor et dolore magna.</q><div class="who">Lorem ipsum dolor</div><div class="readmore">read more... <i>→</i></div></div>
</section>

<section class="newsletter">
  <h2>SUBSCRIBE TO OUR NEWSLETTER</h2>
  <div class="tag">TO RECEIVE THE LATEST NEWS &amp; UPDATE</div>
  <form><div class="field">Your Mail</div><div class="go">SUBMIT</div></form>
</section>

<section class="contact">
  <h2>QUICK CONTACT US</h2>
  <div class="abs input" style="left:98px;top:120px;width:336px">Your Name</div>
  <div class="abs input" style="left:439px;top:120px;width:325px">Your Email</div>
  <div class="abs input" style="left:772px;top:120px;width:327px">Your Subject</div>
  <div class="abs input" style="left:98px;top:171px;width:1001px;height:156px">Your Message...</div>
  <div class="abs submit">SUBMIT</div>
  <div class="abs info" style="left:230px"><div class="ring"><svg width="24" height="32" viewBox="0 0 10 14"><path d="M5 0a5 5 0 0 1 5 5c0 4-5 9-5 9S0 9 0 5a5 5 0 0 1 5-5z" fill="none" stroke="#fff" stroke-width="1.2"/><circle cx="5" cy="5" r="1.8" fill="#fff"/></svg></div>123 Street, City Name, DC 12345</div>
  <div class="abs info" style="left:465px"><div class="ring"><svg width="22" height="34" viewBox="0 0 22 34"><rect x="2" y="2" width="18" height="30" rx="3" fill="none" stroke="#fff" stroke-width="2.5"/><circle cx="11" cy="27" r="2" fill="#fff"/></svg></div>1 234 567 890</div>
  <div class="abs info" style="left:667px"><div class="ring"><svg width="32" height="22" viewBox="0 0 32 22"><rect x="1" y="1" width="30" height="20" rx="2" fill="#fff"/><path d="M2 3 16 13 30 3" fill="none" stroke="#3b3b3d" stroke-width="2"/></svg></div>info@velmarketa.com</div>
  <div class="abs social"><span></span><span></span><span></span><span></span><span></span></div>
</section>

<footer class="site-footer">Copyright © 2007 - Velmarketa Development Group, Inc - All rights reserved</footer>

</body>
</html>
```